New (old) Business Card Design Project

I would like to purchase a customized version of a design you have previously submitted - https://www.artsubmitly.example/design/7395021

I like the card above, and would like to use the same design, jus with my business name, BRADLEY ASSET MANAGEMENT. I like the colors in the card above, as well as the font. The other side will have my name, company name, address, phone, email, website, plus disclosure text I will provide.

Target Market(s)

wealthy families

Industry/Entity Type

Financial Services

Contact Information for Business Card

logo on one side, on other my name, company, address, phone, email, website, disclosure language I will provide.

Colors

Designer to choose colors to be used in the design.

Requirements
Must have
• colors: Deep blue and white
Nice to have
• Please see the items I have uploaded, below.
Should not have
• Cheap, tacky look.

```html
<!DOCTYPE html>
<html lang="en">
<head>
<meta charset="utf-8">
<title>Bradley Asset Management – Business Card</title>
<link rel="stylesheet" href="https://fonts.googleapis.com/css2?family=Cinzel:wght@400;500&family=Montserrat:wght@600&family=Arimo:wght@400&display=swap">
<style>
  :root {
    --deep-blue: #0c2163;
    --label-blue: #2d4a93;
    --paper: #ffffff;
    --ink: #3a3a3a;
    --backdrop: #2a2a2a;
  }
  * { margin: 0; padding: 0; box-sizing: border-box; }
  html, body { width: 1200px; height: 900px; overflow: hidden; background: var(--backdrop); }
  .stage { position: relative; width: 1200px; height: 900px; }
  .card {
    position: absolute; left: 260px; width: 680px; height: 389px;
    background: var(--paper); overflow: hidden;
    box-shadow: 0 10px 30px rgba(0,0,0,0.45);
  }
  .card--front { top: 45px; }
  .card--back { top: 466px; }

  /* Front */
  .front__field {
    position: absolute; left: 0; top: 0; width: 100%; height: 310px;
    background: var(--deep-blue);
    display: flex; align-items: center; justify-content: center;
  }
  .front__name {
    font-family: "Cinzel", serif; font-weight: 400; font-size: 34px;
    letter-spacing: 2px; color: var(--paper); white-space: nowrap;
  }
  .front__tagline {
    position: absolute; left: 0; top: 310px; width: 100%; height: 62px;
    display: flex; align-items: center; justify-content: center; gap: 38px;
    font-family: "Cinzel", serif; font-weight: 500; font-size: 21px;
    letter-spacing: 2px; color: var(--deep-blue); white-space: nowrap;
  }
  .front__tagline .divider { width: 1.5px; height: 22px; background: var(--deep-blue); }
  .front__edge { position: absolute; left: 0; bottom: 0; width: 100%; height: 17px; background: var(--deep-blue); }

  /* Back */
  .back__name {
    position: absolute; left: 40px; top: 58px;
    font-family: "Cinzel", serif; font-weight: 400; font-size: 30px;
    letter-spacing: 2px; color: var(--deep-blue); white-space: nowrap;
  }
  .back__person {
    position: absolute; left: 70px; top: 222px; width: 310px; text-align: right;
    font-family: "Montserrat", sans-serif; font-weight: 600; color: var(--deep-blue);
    white-space: nowrap;
  }
  .back__person .person-name { font-size: 22px; letter-spacing: 1px; }
  .back__person .person-title { font-size: 11px; letter-spacing: 1.5px; margin-top: 2px; }
  .back__rule { position: absolute; left: 400px; top: 190px; width: 2px; height: 150px; background: var(--deep-blue); }
  .back__contact {
    position: absolute; left: 422px; top: 200px;
    font-family: "Arimo", sans-serif; font-size: 15px; line-height: 20px; color: var(--ink);
    white-space: nowrap;
  }
  .back__contact .address { margin-bottom: 14px; }
  .back__contact .label { color: var(--label-blue); }
</style>
</head>
<body>
<main class="stage">
  <section class="card card--front" aria-label="Card front">
    <div class="front__field">
      <span class="front__name">Bradley Asset Management</span>
    </div>
    <div class="front__tagline">
      <span>Plan</span><span class="divider"></span>
      <span>Sustain</span><span class="divider"></span>
      <span>Bequeath</span>
    </div>
    <div class="front__edge"></div>
  </section>

  <section class="card card--back" aria-label="Card back">
    <div class="back__name">Bradley Asset Management</div>
    <div class="back__person">
      <div class="person-name">MARCUS HELBRAND</div>
      <div class="person-title">DIRECTOR</div>
    </div>
    <div class="back__rule"></div>
    <div class="back__contact">
      <div class="address">418 Harbor Lane<br>Kestrel Bay Oregon 97411</div>
      <div><span class="label">phone:</span> 555 014 2280</div>
      <div><span class="label">e-mail:</span> mh@bam-advisors.example</div>
      <div><span class="label">website:</span> www.bam-advisors.example</div>
    </div>
  </section>
</main>
</body>
</html>
```